Environmental Company Website
Kelvro Remediation website
Project: Environmental Company Website
Environmental Company Website - Environment
Creative Brief
Environment
www.kelvroremediation.example
We are an environmental cleanup/spill response company. We service Industrial and Municiple customers. Most of our work revolves around gas/petroleum spills or tank cleaning. We need to keep a very professional, emergency response image. We are not so different than a fire department in our emergency nature. We sell spill supplies to our customers, but we will not sell from our website.
Dislike busy, clumsy, long page websites. Looking for a one page length website (if possible). No scrolling needed to view the pages unless the content demands it. The home page fills the screen, but doesn't go down below the bottom of the window. The nav bar could be on the top or left, whatever best compliments the page.
Elegant
Black / Gray / White/ Blue (see logo)
Yellow
Your choice, we're open to ideas
Arial, Verdana
top
www.lorptank.example
http://www.mavulonsite.example/
http://www.wandertidebreaks.example/
Additional websites we like: http://www.hollisquay-horology.example/en2/ http://www.pinmoorcatch.example/ http://www.oakventhomefit.example/ http://tamworkbuilders.example/ http://www.quennabay.example/ourcatch/

```html
<!DOCTYPE html>
<html lang="en">
<head>
<meta charset="utf-8">
<title>Kelvro Remediation, LLC</title>
<link rel="stylesheet" href="https://fonts.googleapis.com/css2?family=Arimo:wght@400;700&family=Cinzel:wght@400&display=swap">
<style>
:root{
  --bg-light:#f2f2f2;
  --bg-mid:#dcdcdc;
  --ink:#1d1d1d;
  --navy:#1f3a5c;
  --nav-top:#6f7378;
  --nav-bottom:#3c4045;
  --nav-active:#efe2d6;
  --red:#c0341c;
  --orange:#e07a1e;
  --teal:#1f8a7a;
  --panel:#ffffff;
  --welcome-top:#ffffff;
  --welcome-bottom:#d3d3d3;
  --contact-bg:#3e5d86;
  --footer:#2f2f2f;
  --footer-text:#d8d8d8;
  --search:#f0a626;
}
*{box-sizing:border-box;margin:0;padding:0}
html,body{width:1200px;height:993px;overflow:hidden}
body{
  background:radial-gradient(ellipse at 50% 40%,var(--bg-light) 0%,var(--bg-mid) 100%);
  font-family:"Arimo",Arial,sans-serif;color:var(--ink);position:relative;
}
.brand{position:absolute;top:30px;left:0;width:1200px;text-align:center}
.brand-mark{display:block;width:48px;height:48px;border-radius:50%;background:var(--navy);margin:0 auto 10px}
.brand-name{font-family:"Cinzel",Georgia,serif;font-size:30px;color:var(--ink)}
.page{position:absolute;left:126px;top:215px;width:966px;height:555px;background:var(--panel);
  box-shadow:0 0 8px rgba(0,0,0,.18)}
.nav{position:absolute;left:100px;top:134px;width:742px;height:76px;
  background:linear-gradient(var(--nav-top),var(--nav-bottom));border-radius:10px 10px 0 0;
  display:flex;align-items:center;padding:0 14px;box-shadow:0 3px 6px rgba(0,0,0,.3)}
.nav a{color:#fff;text-decoration:none;font-size:15px;font-weight:700;padding:0 18px;
  border-right:1px dotted #9aa0a6;line-height:20px}
.nav a:last-child{border-right:0}
.nav a.active{background:var(--nav-active);color:var(--red);line-height:56px;margin-top:18px;
  border-radius:8px 8px 0 0;padding:0 36px;border-right:0}
.search{position:absolute;left:869px;top:167px;width:188px;height:32px;border:3px solid var(--search);
  border-radius:6px;background:#fff;display:flex;align-items:center}
.search span{flex:1;padding-left:10px;color:#6a8fb8;font-size:14px}
.search b{width:30px;height:100%;background:var(--search);display:flex;align-items:center;justify-content:center}
.welcome{position:absolute;left:178px;top:231px;width:858px;height:186px;
  background:linear-gradient(var(--welcome-top),var(--welcome-bottom));border:1px solid #bbb}
.contact{position:absolute;left:10px;top:6px;width:210px;height:172px;background:var(--contact-bg);
  border:2px solid #a9b9cc;padding:6px 14px;color:#fff}
.contact h3{font-size:13px;text-align:center;margin-bottom:6px}
.field{background:#fff;color:#333;font-size:12px;padding:1px 5px;height:18px;margin-bottom:5px;border:1px solid #8aa}
.field.msg{height:44px}
.submit{display:block;margin:8px auto 0;width:72px;height:22px;background:var(--red);color:#fff;
  font-size:11px;font-weight:700;text-align:center;line-height:22px;border-radius:10px;border:2px solid #e8c9a8}
.intro{position:absolute;left:234px;top:14px;width:600px}
.intro h2{font-size:19px;color:var(--red);margin-bottom:6px}
.intro h2 span{color:var(--navy)}
.intro p{font-size:13px;line-height:16px;text-align:justify}
.more{position:absolute;left:731px;top:129px;width:95px;height:30px;background:#7a7a7a;border:3px solid var(--search);
  color:var(--ink);font-size:12px;font-weight:700;text-align:center;line-height:24px}
.tail{position:absolute;left:735px;top:185px}
.services-title{position:absolute;left:412px;top:426px;font-size:19px;font-weight:700;color:var(--red)}
.services-title span{color:var(--navy)}
.strip{position:absolute;left:178px;top:471px;width:861px;height:261px;display:flex;gap:6px;
  background:#c8cdd2;padding:4px;border:1px solid #999}
.tile{flex:1;display:flex}
.label{width:36px;color:#fff;font-size:15px;font-weight:700;writing-mode:vertical-rl;transform:rotate(180deg);
  display:flex;align-items:center;justify-content:center}
.label.teal{background:var(--teal)}.label.orange{background:var(--orange)}
.photo{flex:1}
.p1{background:linear-gradient(#4f86c6,#c9762e 70%,#2d4f7a)}
.p2{background:linear-gradient(#d9d4c6,#8e9ca4 60%,#3f5a68)}
.p3{background:linear-gradient(#5a8c2e,#d8b41a 55%,#6e7f35)}
.p4{background:linear-gradient(#9cc3e8,#e6eef5 60%,#7e8a96)}
.footer{position:absolute;left:126px;top:770px;width:966px;height:91px;background:var(--footer);padding:22px 50px;color:var(--footer-text)}
.footer nav{font-size:11px}
.footer small{display:block;font-size:9px;margin-top:6px;color:#9a9a9a}
.footer .fname{position:absolute;right:60px;top:32px;font-family:"Cinzel",Georgia,serif;font-size:16px;color:#fff}
</style>
</head>
<body>
<header class="brand">
  <span class="brand-mark"></span>
  <div class="brand-name">Kelvro Remediation, LLC</div>
</header>

<div class="page"></div>

<nav class="nav">
  <a class="active" href="#">HOME</a>
  <a href="#">ABOUT US</a>
  <a href="#">SPILL RESPONSES</a>
  <a href="#">EQUIPMENT</a>
  <a href="#">SERVICES</a>
  <a href="#">CONTACT</a>
</nav>
<div class="search"><span>SEARCH</span><b><svg width="14" height="14" viewBox="0 0 14 14"><circle cx="6" cy="6" r="4" fill="none" stroke="#fff" stroke-width="2"/><line x1="9" y1="9" x2="13" y2="13" stroke="#fff" stroke-width="2"/></svg></b></div>

<section class="welcome">
  <form class="contact">
    <h3>CONTACT US</h3>
    <div class="field">Name</div>
    <div class="field">E-Mail</div>
    <div class="field msg">Message</div>
    <span class="submit">SUBMIT</span>
  </form>
  <div class="intro">
    <h2>Welcome <span>To Our Site !</span></h2>
    <p>We are an environmental cleanup/spill response company. We service Industrial and Municiple customers. Most of our work revolves around gas/petroleum spills or tank cleaning. We need to keep a very professional, emergency response image. We are not so different than a fire department in our emergency nature. We sell spill supplies to our customers, but we will not sell from our website.</p>
  </div>
  <span class="more">READ MORE</span>
  <svg class="tail" width="40" height="36" viewBox="0 0 40 36"><path d="M0 0 L30 0 L4 34 Z" fill="#d3d3d3" stroke="#bbb"/></svg>
</section>

<h2 class="services-title">24 Hours <span>Response Services For :</span></h2>

<section class="strip">
  <div class="tile"><div class="photo p1" role="img" aria-label="Offshore oil platform at sea"></div><div class="label teal">Offshore Spill</div></div>
  <div class="tile"><div class="label orange">Oil Spill</div><div class="photo p2" role="img" aria-label="White birds standing in oily marsh water"></div></div>
  <div class="tile"><div class="label teal">Radiation Spill</div><div class="photo p3" role="img" aria-label="Yellow hazard barrels with radiation signs"></div></div>
  <div class="tile"><div class="label orange">Chemical Response</div><div class="photo p4" role="img" aria-label="Responders in protective suits cleaning a spill"></div></div>
</section>

<footer class="footer">
  <nav>Home | About Us | Spill Responses | Equipment | Services | Clean Up &amp; Responses | Contact</nav>
  <small>© 2013 Kelvro Remediation, LLC. All rights reserved</small>
  <span class="fname">Kelvro Remediation, LLC</span>
</footer>
</body>
</html>
```